MOLT - Monitoring Natural Hazards from Space Web Application

KORVEN Sarl is a Luxembourg based Space-Startup that works in the field of Earth Observation. KORVEN is a platform able to extract value-added information from satellite data and is specialized in mapping Natural Disaster (floods, fires etc).

We are now developing a new vertical tool, called MOLT, dedicated to the monitoring of natural hazards in Humanitarian Camps around the world.

The goal of MOLT is to hide to the users' all the complexity of the Satellite Image processing and just provide them the results.

This project require to Design 4 pages of MOLT:
• Public Home Page (Code - V01)
• Dashboard (private Home Page) (Code - V03)
• Monitor (web GIS) (Code - V14)
• Registration Page (Code - V04)

We would like to provide the required time to make a good job.

Target Market(s)

Humanitarian Agencies, Goverments

Coding

Coded - Design and coding required

Number of Pages Required

4 page

Font styles to use
Other font styles liked:
• see the manual attached

Requirements
Must have
• 4 pages. One Home, one form, one dashboard and one web map.
Nice to have
• Please read the attachment with all the detailed instructions

```html
<!DOCTYPE html>
<html lang="en">
<head>
<meta charset="utf-8">
<title>MOLT – Monitor</title>
<link rel="stylesheet" href="https://fonts.googleapis.com/css2?family=Jost:wght@400;500;600&family=Space+Mono&display=swap">
<style>
  :root {
    --bg: #f1f1f1;
    --app: #f8f8f8;
    --panel: #ffffff;
    --line: #e4e4e4;
    --ink: #111111;
    --ink-soft: #444a52;
    --brand: #e9b42c;
    --accent: #f0b92c;
    --pin: #3e5a66;
    --alert: #f0527a;
    --map: #d5d5d5;
    --grey-block: #d9d9d9;
  }
  * { box-sizing: border-box; margin: 0; padding: 0; }
  html, body { width: 1200px; height: 675px; overflow: hidden; }
  body {
    background: radial-gradient(circle at 50% 50%, #f7f7f7 0%, var(--bg) 100%);
    font-family: "Jost", sans-serif;
    color: var(--ink);
    position: relative;
  }
  .app {
    position: absolute; left: 150px; top: 56px; width: 900px; height: 563px;
    background: var(--app);
    box-shadow: 0 6px 30px rgba(0,0,0,0.05);
    overflow: hidden;
  }
  .abs { position: absolute; }
  .brand { left: 11px; top: 13px; display: flex; align-items: center; gap: 8px; }
  .brand-dot { width: 30px; height: 30px; border: 2px solid var(--brand); border-radius: 50%; }
  .brand-name { font-size: 22px; font-weight: 400; color: var(--pin); letter-spacing: 3px; }

  .top-btn {
    top: 11px; height: 34px; background: var(--panel); border: 1px solid var(--line);
    display: flex; align-items: center; justify-content: center; gap: 6px;
    color: var(--ink-soft); font-size: 10.5px;
  }
  .top-btn svg { width: 16px; height: 16px; }
  .btn-notify { left: 611px; width: 91px; }
  .btn-help { left: 711px; width: 58px; }
  .btn-account { left: 777px; width: 96px; color: var(--ink); font-size: 15px; font-weight: 500; }

  .search {
    left: 129px; top: 65px; width: 744px; height: 34px; background: var(--panel);
    border: 1px solid var(--line); display: flex; align-items: center; padding-left: 16px;
    font-size: 15px; font-weight: 500;
  }
  .add-area {
    position: absolute; right: 4px; top: 4px; width: 79px; height: 24px; background: var(--accent);
    display: flex; align-items: center; justify-content: center; font-size: 13px; font-weight: 500;
  }

  .map { left: 129px; top: 111px; width: 537px; height: 299px; background: var(--map); overflow: hidden; border: 1px solid #cfcfcf; }
  .map-fill { position: absolute; inset: 0; background: linear-gradient(160deg, #dedede 0%, #d2d2d2 100%); }
  .map-toggle { position: absolute; left: 421px; top: 12px; display: flex; height: 21px; background: var(--panel); box-shadow: 0 1px 3px rgba(0,0,0,.15); }
  .map-toggle span { font-size: 10px; display: flex; align-items: center; padding: 0 11px; }
  .map-toggle span + span { border-left: 1px solid var(--line); }
  .zoom { position: absolute; left: 496px; top: 232px; width: 29px; height: 54px; background: var(--panel); box-shadow: 0 1px 3px rgba(0,0,0,.15); display: flex; flex-direction: column; }
  .zoom span { flex: 1; display: flex; align-items: center; justify-content: center; font-size: 16px; font-weight: 500; }
  .zoom span + span { border-top: 1px solid var(--line); }
  .map-marks { position: absolute; inset: 0; }

  .news { left: 689px; top: 111px; width: 184px; height: 217px; background: #f4f4f4; border: 1px solid var(--line); padding: 12px 14px; }
  .news h2 { font-size: 15.5px; font-weight: 500; margin-bottom: 6px; }
  .news-item { position: relative; height: 30px; background: var(--panel); border: 1px solid #ececec; margin-bottom: 11px; display: flex; align-items: center; padding-left: 6px; font-size: 7.5px; }
  .news-date { position: absolute; right: 4px; top: 3px; font-size: 3px; color: #bbb; }
  .grey-block { left: 689px; top: 348px; width: 184px; height: 62px; background: var(--grey-block); }

  .details { left: 129px; top: 425px; width: 744px; height: 105px; background: var(--panel); border: 1px solid #efefef; }
  .area { position: absolute; left: 17px; top: 18px; }
  .area h1 { font-size: 23px; font-weight: 500; line-height: 1.1; }
  .area p { font-size: 15px; line-height: 1.2; }
  .stat { position: absolute; top: 9px; width: 132px; height: 87px; border: 1px solid var(--line); padding: 8px 11px; overflow: hidden; }
  .stat-head { display: flex; align-items: center; gap: 7px; font-size: 22px; line-height: 1; }
  .stat-head svg { width: 20px; height: 20px; flex: none; }
  .stat-value { font-size: 25px; margin-top: 8px; line-height: 1; }
  .stat-caption { font-size: 3.4px; line-height: 1.4; margin-top: 8px; }
  .people { left: 169px; }
  .time { left: 311px; }
  .notes { left: 454px; }
  .images { left: 597px; }
  .notes-text { font-size: 3.2px; line-height: 1.5; margin-top: 7px; }
  .thumbs { display: grid; grid-template-columns: repeat(3, 33px); gap: 3px; margin-top: 5px; margin-left: 2px; }
  .thumb { height: 23px; }
  .t1 { background: linear-gradient(135deg,#7c6a52,#5b6b5a); }
  .t2 { background: linear-gradient(135deg,#8a96a3,#5d5f62); }
  .t3 { background: linear-gradient(135deg,#7a6a56,#4f5a58); }
  .t4 { background: linear-gradient(135deg,#5e7a95,#7a6a4e); }
  .t5 { background: linear-gradient(135deg,#b89a78,#8a6a50); }
  .t6 { background: linear-gradient(135deg,#5c6f78,#7d6c56); }

  .support { left: 11px; top: 528px; display: flex; align-items: center; gap: 7px; font-size: 10.5px; color: var(--ink-soft); }
  .support svg { width: 19px; height: 19px; }
  .legal { top: 542px; font-family: "Space Mono", monospace; font-size: 6.5px; color: #888; }
</style>
</head>
<body>
<div class="app">
  <div class="abs brand"><span class="brand-dot"></span><span class="brand-name">MOLT</span></div>

  <div class="abs top-btn btn-notify">
    <svg viewBox="0 0 16 16" fill="none" stroke="#222" stroke-width="1.2"><circle cx="8" cy="8" r="7"/><line x1="8" y1="7" x2="8" y2="11.5"/><circle cx="8" cy="4.8" r=".5" fill="#222"/></svg>Notifications
  </div>
  <div class="abs top-btn btn-help">
    <svg viewBox="0 0 16 16" fill="none" stroke="#222" stroke-width="1.2"><circle cx="8" cy="8" r="7"/><line x1="8" y1="7" x2="8" y2="11.5"/><circle cx="8" cy="4.8" r=".5" fill="#222"/></svg>Help
  </div>
  <div class="abs top-btn btn-account">
    <svg viewBox="0 0 16 16" fill="none" stroke="#111" stroke-width="1.2"><circle cx="8" cy="8" r="7"/><circle cx="8" cy="6.3" r="2.4"/><path d="M3.6 12.8c1.2-2 2.6-2.8 4.4-2.8s3.2.8 4.4 2.8"/></svg>Account
  </div>

  <div class="abs search">Search<div class="add-area">+ Add Area</div></div>

  <div class="abs map">
    <div class="map-fill" role="img" aria-label="Grey world map showing monitored camp locations"></div>
    <svg class="map-marks" viewBox="0 0 537 299">
      <circle cx="278" cy="174" r="23" fill="none" stroke="var(--alert)" stroke-width=".6"/>
      <circle cx="278" cy="174" r="16" fill="none" stroke="var(--alert)" stroke-width=".6"/>
      <circle cx="278" cy="174" r="9" fill="var(--alert)"/>
      <g fill="var(--pin)">
        <path d="M83 52c-9.5 0-17.5 7.5-17.5 17 0 12 17.5 24 17.5 24s17.5-12 17.5-24c0-9.5-8-17-17.5-17z"/>
        <path d="M397 72c-9.5 0-17.5 7.5-17.5 17 0 12 17.5 24 17.5 24s17.5-12 17.5-24c0-9.5-8-17-17.5-17z"/>
        <path d="M278 132c-9.5 0-17.5 7.5-17.5 17 0 12 17.5 24 17.5 24s17.5-12 17.5-24c0-9.5-8-17-17.5-17z"/>
      </g>
      <g fill="#fff"><circle cx="83" cy="69" r="7.5"/><circle cx="397" cy="89" r="7.5"/><circle cx="278" cy="149" r="7.5"/></g>
    </svg>
    <div class="map-toggle"><span>Map</span><span>Satellite</span></div>
    <div class="zoom"><span>+</span><span>−</span></div>
  </div>

  <div class="abs news">
    <h2>News Alert</h2>
    <div class="news-item"><span class="news-date">21/08/2024</span>Flood in South London</div>
    <div class="news-item"><span class="news-date">21/08/2024</span>Flood in South London</div>
    <div class="news-item"><span class="news-date">21/08/2024</span>Flood in South London</div>
  </div>
  <div class="abs grey-block"></div>

  <div class="abs details">
    <div class="area"><h1>Area name</h1><p>Event: Flood</p></div>

    <div class="stat people">
      <div class="stat-head"><svg viewBox="0 0 24 24" fill="none" stroke="#111" stroke-width="1"><circle cx="12" cy="8" r="3"/><circle cx="5" cy="10" r="2.2"/><circle cx="19" cy="10" r="2.2"/><path d="M7 19c0-3 2.2-5.5 5-5.5s5 2.5 5 5.5M1.5 18c0-2.3 1.5-4 3.5-4M22.5 18c0-2.3-1.5-4-3.5-4"/></svg>People</div>
      <div class="stat-value">564.000</div>
      <div class="stat-caption">The town has over 2 million population, more than half a million of them are affected</div>
    </div>

    <div class="stat time">
      <div class="stat-head"><svg viewBox="0 0 24 24" fill="none" stroke="#111" stroke-width="1"><circle cx="12" cy="12" r="10.5"/><path d="M12 5v7h5"/></svg>Time</div>
      <div class="stat-value">22h ago</div>
      <div class="stat-caption">The event was first recorded on 12:32:05, 22/08/2024</div>
    </div>

    <div class="stat notes">
      <div class="stat-head"><svg viewBox="0 0 24 24" fill="none" stroke="#111" stroke-width="1"><rect x="4" y="3" width="16" height="19" rx="1"/><path d="M9 3V1.5h6V3M8 11h6M8 15h8"/></svg>Notes</div>
      <div class="notes-text">overflow of large amounts of water on the earth's surface, causing destruction. Floods can occur due to many reasons like as a result of strong rains, incoming waves from the ocean, or the failure of dams or levees. Floods can happen suddenly or gradually over a long period and can last up to many days or weeks or even longer, depending upon the type and extent of the flood. Out of all the natural disasters, floods are the most common, seen all over the country at certain times.</div>
    </div>

    <div class="stat images">
      <div class="stat-head"><svg viewBox="0 0 24 24" fill="none" stroke="#111" stroke-width="1"><rect x="2" y="3" width="20" height="18"/><circle cx="16" cy="8" r="2"/><path d="M2 17l6-6 8 8"/></svg>Images</div>
      <div class="thumbs">
        <div class="thumb t1" role="img" aria-label="Aerial photo of flooded streets"></div>
        <div class="thumb t2" role="img" aria-label="Photo of a flooded house"></div>
        <div class="thumb t3" role="img" aria-label="Photo of flood debris"></div>
        <div class="thumb t4" role="img" aria-label="Photo of residents crossing floodwater"></div>
        <div class="thumb t5" role="img" aria-label="Photo of a muddy flooded road"></div>
        <div class="thumb t6" role="img" aria-label="Photo of a flooded town square"></div>
      </div>
    </div>
  </div>

  <div class="abs support">
    <svg viewBox="0 0 20 20" fill="none" stroke="#222" stroke-width="1"><circle cx="10" cy="10" r="9"/><path d="M5 11V9a5 5 0 0 1 10 0v2"/><rect x="4.5" y="10" width="2.5" height="4" rx="1"/><rect x="13" y="10" width="2.5" height="4" rx="1"/></svg>Support
  </div>
  <div class="abs legal" style="left:664px">Terms of Service</div>
  <div class="abs legal" style="left:740px">Privacy Policy</div>
  <div class="abs legal" style="left:809px">Copyright 2024</div>
</div>
</body>
</html>
```